Business card design needed

We are a gardening company who handle:
All Forms of gardens work including
Mowing
Pruning
edging
weeding
Poisoning
Landscaping
Minor Stump Removal
Rubbish Removal
and more

I want a card that look professional not cartoon style

Industry/Entity Type

Business

Contact Information for Business Card

Fernhollow Yard and Lawn Service

Greg Halden
0486152938

```html
<!DOCTYPE html>
<html lang="en">
<head>
<meta charset="utf-8">
<title>Fernhollow Yard and Lawn Service – Business Card</title>
<link href="https://fonts.googleapis.com/css2?family=Oswald:wght@400;500;700&display=swap" rel="stylesheet">
<style>
  :root {
    --backdrop: #d9d9d9;
    --card: #fbfbfb;
    --ink: #161616;
    --accent: #c0242f;
    --band: #1b1b1b;
  }
  html, body {
    margin: 0;
    width: 1200px;
    height: 871px;
    overflow: hidden;
    background: var(--backdrop);
  }
  .business-card {
    position: absolute;
    left: 100px;
    top: 150px;
    width: 1000px;
    height: 572px;
    background: var(--card);
    box-shadow: 0 10px 30px rgba(0,0,0,0.25);
    overflow: hidden;
    font-family: "Oswald", sans-serif;
    color: var(--ink);
  }
  .company-name {
    position: absolute;
    left: 200px;
    top: 52px;
    margin: 0;
    font-size: 42px;
    font-weight: 700;
    letter-spacing: 0.5px;
    text-transform: uppercase;
  }
  .contact-list {
    position: absolute;
    left: 0;
    top: 165px;
    margin: 0;
    padding: 0;
    list-style: none;
  }
  .contact-row {
    display: flex;
    align-items: center;
    height: 42px;
  }
  .contact-marker {
    width: 72px;
    height: 30px;
    background: var(--band);
    margin-right: 14px;
  }
  .contact-label {
    width: 150px;
    color: var(--accent);
    font-size: 21px;
    font-weight: 500;
    text-transform: uppercase;
  }
  .contact-value {
    font-size: 20px;
    font-weight: 500;
    line-height: 1.05;
    text-transform: uppercase;
  }
  .signature {
    position: absolute;
    right: 90px;
    top: 350px;
    display: flex;
    align-items: center;
  }
  .person-name {
    font-size: 44px;
    font-weight: 700;
    text-transform: uppercase;
    padding-right: 12px;
    border-right: 2px solid var(--ink);
    line-height: 1;
  }
  .person-role {
    padding-left: 12px;
    color: var(--accent);
    font-size: 24px;
    font-weight: 500;
    text-transform: uppercase;
    margin-top: 22px;
  }
  .card-base {
    position: absolute;
    left: 0;
    bottom: 0;
    width: 1000px;
    height: 160px;
  }
</style>
</head>
<body>
  <div class="business-card">
    <h1 class="company-name">Fernhollow Yard and Lawn Service</h1>

    <ul class="contact-list">
      <li class="contact-row">
        <span class="contact-marker"></span>
        <span class="contact-label">Adress</span>
        <span class="contact-value">418 Birchmoor Lane, Ashcombe<br>Valeria, 40218</span>
      </li>
      <li class="contact-row">
        <span class="contact-marker"></span>
        <span class="contact-label">Phone</span>
        <span class="contact-value">0486152938</span>
      </li>
      <li class="contact-row">
        <span class="contact-marker"></span>
        <span class="contact-label">E-mail</span>
        <span class="contact-value">info@domain.com</span>
      </li>
      <li class="contact-row">
        <span class="contact-marker"></span>
        <span class="contact-label">Website</span>
        <span class="contact-value">www.yourcompany.com</span>
      </li>
    </ul>

    <div class="signature">
      <span class="person-name">Greg Halden</span>
      <span class="person-role">General Manager</span>
    </div>

    <svg class="card-base" viewBox="0 0 1000 160" aria-hidden="true">
      <line x1="0" y1="12" x2="1000" y2="12" stroke="var(--accent)" stroke-width="4"/>
      <rect x="0" y="40" width="1000" height="120" fill="var(--band)"/>
      <polygon points="600,18 800,18 690,110" fill="var(--band)"/>
      <line x1="640" y1="18" x2="690" y2="110" stroke="var(--card)" stroke-width="8"/>
      <line x1="690" y1="110" x2="800" y2="40" stroke="var(--card)" stroke-width="8"/>
    </svg>
  </div>
</body>
</html>
```